Home brewer beer bottle label

I need a label for home-brew beer bottles. My sons and I all make our own beer. It should say Frask Ale in blackletter (because we are of German heritage) (EDIT: ACTUALLY WE ARE LIKING OTHER TYPEFACE NOW) and the designer will need to work in aspects of the Frask family (crest attached). Finally we will need two blank areas or lines for (1) what kind of beer (handwritten) and (2) who made it (the Hopwright!) I have attached a rough sketch, but feel free to ignore and be creative. No color requirements. (EDIT: ACTUALLY, MY WIFE LIKES THE LITTLE BIT OF PURPLE IN THE 4TH DESIGN) Would like the logotype portion of the label to be usable on its own as a family logo. (EDIT; THIS IS LESS IMPORTANT NOW). I have attached another file sketch, which shows using the parts of the family crest w/out trying to replicate it. Thanks, everyone, for the good work....
Updates

Project Deadline Extended
Reason: Extending because my wife is out of town until Wednesday and I need her input.

Target Market(s)

Mostly friends and family at the wedding.

Industry/Entity Type

Work

Font styles to use
Serif
Sans Serif

Requirements
Must have
• Tightly kerned lettering,
Nice to have
• Color, one Group of Elements in Indesign and the print file, "Beer" and "Hopwright" lines
Should not have
• Hard to see logo or logo type

```html
<!DOCTYPE html>
<html lang="en">
<head>
<meta charset="utf-8">
<title>Frask Ale – Bottle Label Options</title>
<link href="https://fonts.googleapis.com/css2?family=UnifrakturCook:wght@700&family=Alfa+Slab+One&family=Open+Sans:wght@400&family=Petit+Formal+Script&display=swap" rel="stylesheet">
<style>
  :root{
    --ink:#1a1a1a;
    --brand-blue:#2f5fe0;
    --ring-gold:#e0a830;
    --panel-gold:#d9b85a;
    --line:#6b5a2a;
    --gold:linear-gradient(90deg,#6b5a1e 0%,#b8a35a 25%,#efe4a8 50%,#b8a35a 75%,#6b5a1e 100%);
    --sky:linear-gradient(90deg,#6fe0fb 0%,#3fb0f5 45%,#2a8ff0 100%);
    --lime:linear-gradient(90deg,#9af52a 0%,#86ee16 50%,#a0f53a 100%);
    --grass:linear-gradient(90deg,#2e9a2a 0%,#5cc83a 50%,#7ddc48 100%);
    --coal:linear-gradient(90deg,#222 0%,#4a4a4a 50%,#5a5c5c 100%);
    --silver:linear-gradient(90deg,#c4c4c4 0%,#dedede 50%,#cfcfcf 100%);
    --teal:#3cc4c8;
  }
  *{box-sizing:border-box;margin:0;padding:0}
  html,body{width:1200px;height:964px;overflow:hidden;background:#fff}
  body{position:relative;font-family:"Open Sans",sans-serif;color:var(--ink)}

  .section-title{position:absolute;font-size:15px;font-weight:400}

  .pair{position:absolute;display:flex;gap:6px}
  .tag{position:relative;width:121px;height:180px;border-radius:22px 22px 16px 16px / 34px 34px 18px 18px;
       box-shadow:4px 6px 8px rgba(0,0,0,.35)}
  .gold{background:var(--gold)} .sky{background:var(--sky)} .lime{background:var(--lime)}
  .grass{background:var(--grass)} .coal{background:var(--coal)} .silver{background:var(--silver)}

  .hole{position:absolute;top:9px;width:7px;height:7px;border-radius:50%;background:#555}
  .front .hole{left:33px} .back .hole{right:33px}

  .seal{position:absolute;left:50%;transform:translateX(-50%);width:90px;height:90px;border-radius:50%;
        background:radial-gradient(circle,#fff 60%,#dfe6f5 100%);border:3px solid var(--ring-gold);
        display:flex;align-items:center;justify-content:center}
  .seal span{font-family:"Alfa Slab One",serif;font-size:17px;color:var(--brand-blue)}
  .front .seal{top:14px}

  .name{position:absolute;left:0;right:0;text-align:center;color:var(--brand-blue);letter-spacing:-.5px}
  .name.gothic{font-family:"UnifrakturCook",serif;font-weight:700;font-size:26px;line-height:27px;top:114px}
  .name.slab{font-family:"Alfa Slab One",serif;font-size:19px;line-height:21px;top:120px}

  .back svg{position:absolute;inset:0}
  .field-label{font-family:"Petit Formal Script",cursive;font-size:8px;fill:var(--ink)}

  .sheet{position:absolute;top:685px;width:146px;height:225px;box-shadow:1px 1px 2px rgba(0,0,0,.3)}
  .sheet .seal{top:22px;width:88px;height:88px}
  .sheet .plain-mark{position:absolute;top:20px;left:50%;transform:translateX(-50%);width:70px;height:70px;
        background:var(--brand-blue);border:2px solid var(--ring-gold)}
  .corner-band{position:absolute;top:0;left:0;width:70px;height:26px;background:var(--teal);
        clip-path:polygon(0 0,100% 0,0 100%)}
  .sheet .name.gothic{top:116px;font-size:24px;line-height:26px;white-space:nowrap}
  .sheet .name.slab{top:118px;font-size:18px;line-height:20px}
  .entry{position:absolute;left:8px;right:8px;display:flex;align-items:flex-end;gap:4px;
         font-family:"Petit Formal Script",cursive;font-size:8px}
  .entry::before{content:"";width:6px;height:6px;border:1px solid var(--ink);background:#fff;flex:none}
  .entry i{flex:1;border-bottom:1px solid var(--line);height:1px;margin-left:6px}
  .entry.beer{top:172px} .entry.maker{top:207px}
</style>
</head>
<body>

<p class="section-title" style="left:30px;top:36px">Double sided:</p>

<!-- Tag pairs -->
<div class="pair" style="left:31px;top:72px">
  <div class="tag gold front"><span class="hole"></span><div class="seal"><span>Frask</span></div><p class="name gothic">Frask<br>Ale</p></div>
  <div class="tag gold back"><span class="hole"></span><svg viewBox="0 0 121 180"><path d="M60.5 168 L14 115 C0 90 4 20 60.5 14 C117 20 121 90 107 115 Z" fill="var(--panel-gold)" stroke="#fff" stroke-width="2"/><polygon points="20,122 101,122 60.5,168" fill="var(--brand-blue)"/><text class="field-label" x="60.5" y="40" text-anchor="middle">Beer</text><path d="M60.5 44v7m-2-2 2 2 2-2" stroke="#111" fill="none"/><line x1="24" y1="71" x2="97" y2="71" stroke="var(--line)" stroke-width=".6"/><text class="field-label" x="60.5" y="86" text-anchor="middle">Hopwright</text><path d="M60.5 90v7m-2-2 2 2 2-2" stroke="#111" fill="none"/><line x1="20" y1="114" x2="101" y2="114" stroke="var(--line)" stroke-width=".6"/></svg></div>
</div>
<div class="pair" style="left:306px;top:72px">
  <div class="tag sky front"><span class="hole"></span><div class="seal"><span>Frask</span></div><p class="name gothic">Frask<br>Ale</p></div>
  <div class="tag sky back"><span class="hole"></span><svg viewBox="0 0 121 180"><path d="M60.5 168 L14 115 C0 90 4 20 60.5 14 C117 20 121 90 107 115 Z" fill="var(--panel-gold)" stroke="#fff" stroke-width="2"/><polygon points="20,122 101,122 60.5,168" fill="var(--brand-blue)"/><text class="field-label" x="60.5" y="40" text-anchor="middle">Beer</text><path d="M60.5 44v7m-2-2 2 2 2-2" stroke="#111" fill="none"/><line x1="24" y1="71" x2="97" y2="71" stroke="var(--line)" stroke-width=".6"/><text class="field-label" x="60.5" y="86" text-anchor="middle">Hopwright</text><path d="M60.5 90v7m-2-2 2 2 2-2" stroke="#111" fill="none"/><line x1="20" y1="114" x2="101" y2="114" stroke="var(--line)" stroke-width=".6"/></svg></div>
</div>
<div class="pair" style="left:594px;top:68px">
  <div class="tag gold front"><span class="hole"></span><div class="seal"><span>Frask</span></div><p class="name slab">Frask<br>Ale</p></div>
  <div class="tag gold back"><span class="hole"></span><svg viewBox="0 0 121 180"><path d="M60.5 168 L14 115 C0 90 4 20 60.5 14 C117 20 121 90 107 115 Z" fill="var(--panel-gold)" stroke="#fff" stroke-width="2"/><polygon points="20,122 101,122 60.5,168" fill="var(--brand-blue)"/><text class="field-label" x="60.5" y="40" text-anchor="middle">Beer</text><path d="M60.5 44v7m-2-2 2 2 2-2" stroke="#111" fill="none"/><line x1="24" y1="71" x2="97" y2="71" stroke="var(--line)" stroke-width=".6"/><text class="field-label" x="60.5" y="86" text-anchor="middle">Hopwright</text><path d="M60.5 90v7m-2-2 2 2 2-2" stroke="#111" fill="none"/><line x1="20" y1="114" x2="101" y2="114" stroke="var(--line)" stroke-width=".6"/></svg></div>
</div>
<div class="pair" style="left:898px;top:68px">
  <div class="tag sky front"><span class="hole"></span><div class="seal"><span>Frask</span></div><p class="name slab">Frask<br>Ale</p></div>
  <div class="tag sky back"><span class="hole"></span><svg viewBox="0 0 121 180"><path d="M60.5 168 L14 115 C0 90 4 20 60.5 14 C117 20 121 90 107 115 Z" fill="var(--panel-gold)" stroke="#fff" stroke-width="2"/><polygon points="20,122 101,122 60.5,168" fill="var(--brand-blue)"/><text class="field-label" x="60.5" y="40" text-anchor="middle">Beer</text><path d="M60.5 44v7m-2-2 2 2 2-2" stroke="#111" fill="none"/><line x1="24" y1="71" x2="97" y2="71" stroke="var(--line)" stroke-width=".6"/><text class="field-label" x="60.5" y="86" text-anchor="middle">Hopwright</text><path d="M60.5 90v7m-2-2 2 2 2-2" stroke="#111" fill="none"/><line x1="20" y1="114" x2="101" y2="114" stroke="var(--line)" stroke-width=".6"/></svg></div>
</div>

<div class="pair" style="left:31px;top:346px">
  <div class="tag lime front"><span class="hole"></span><div class="seal"><span>Frask</span></div><p class="name gothic">Frask<br>Ale</p></div>
  <div class="tag lime back"><span class="hole"></span><svg viewBox="0 0 121 180"><path d="M60.5 168 L14 115 C0 90 4 20 60.5 14 C117 20 121 90 107 115 Z" fill="var(--panel-gold)" stroke="#fff" stroke-width="2"/><polygon points="20,122 101,122 60.5,168" fill="var(--brand-blue)"/><text class="field-label" x="60.5" y="40" text-anchor="middle">Beer</text><path d="M60.5 44v7m-2-2 2 2 2-2" stroke="#111" fill="none"/><line x1="24" y1="71" x2="97" y2="71" stroke="var(--line)" stroke-width=".6"/><text class="field-label" x="60.5" y="86" text-anchor="middle">Hopwright</text><path d="M60.5 90v7m-2-2 2 2 2-2" stroke="#111" fill="none"/><line x1="20" y1="114" x2="101" y2="114" stroke="var(--line)" stroke-width=".6"/></svg></div>
</div>
<div class="pair" style="left:306px;top:344px">
  <div class="tag grass front"><span class="hole"></span><div class="seal"><span>Frask</span></div><p class="name gothic">Frask<br>Ale</p></div>
  <div class="tag grass back"><span class="hole"></span><svg viewBox="0 0 121 180"><path d="M60.5 168 L14 115 C0 90 4 20 60.5 14 C117 20 121 90 107 115 Z" fill="var(--panel-gold)" stroke="#fff" stroke-width="2"/><polygon points="20,122 101,122 60.5,168" fill="var(--brand-blue)"/><text class="field-label" x="60.5" y="40" text-anchor="middle">Beer</text><path d="M60.5 44v7m-2-2 2 2 2-2" stroke="#111" fill="none"/><line x1="24" y1="71" x2="97" y2="71" stroke="var(--line)" stroke-width=".6"/><text class="field-label" x="60.5" y="86" text-anchor="middle">Hopwright</text><path d="M60.5 90v7m-2-2 2 2 2-2" stroke="#111" fill="none"/><line x1="20" y1="114" x2="101" y2="114" stroke="var(--line)" stroke-width=".6"/></svg></div>
</div>
<div class="pair" style="left:594px;top:338px">
  <div class="tag coal front"><span class="hole"></span><div class="seal"><span>Frask</span></div><p class="name slab">Frask<br>Ale</p></div>
  <div class="tag coal back"><span class="hole"></span><svg viewBox="0 0 121 180"><path d="M60.5 168 L14 115 C0 90 4 20 60.5 14 C117 20 121 90 107 115 Z" fill="var(--panel-gold)" stroke="#fff" stroke-width="2"/><polygon points="20,122 101,122 60.5,168" fill="var(--brand-blue)"/><text class="field-label" x="60.5" y="40" text-anchor="middle">Beer</text><path d="M60.5 44v7m-2-2 2 2 2-2" stroke="#111" fill="none"/><line x1="24" y1="71" x2="97" y2="71" stroke="var(--line)" stroke-width=".6"/><text class="field-label" x="60.5" y="86" text-anchor="middle">Hopwright</text><path d="M60.5 90v7m-2-2 2 2 2-2" stroke="#111" fill="none"/><line x1="20" y1="114" x2="101" y2="114" stroke="var(--line)" stroke-width=".6"/></svg></div>
</div>
<div class="pair" style="left:898px;top:340px">
  <div class="tag silver front"><span class="hole"></span><div class="seal"><span>Frask</span></div><p class="name slab">Frask<br>Ale</p></div>
  <div class="tag silver back"><span class="hole"></span><svg viewBox="0 0 121 180"><path d="M60.5 168 L14 115 C0 90 4 20 60.5 14 C117 20 121 90 107 115 Z" fill="var(--panel-gold)" stroke="#fff" stroke-width="2"/><polygon points="20,122 101,122 60.5,168" fill="var(--brand-blue)"/><text class="field-label" x="60.5" y="40" text-anchor="middle">Beer</text><path d="M60.5 44v7m-2-2 2 2 2-2" stroke="#111" fill="none"/><line x1="24" y1="71" x2="97" y2="71" stroke="var(--line)" stroke-width=".6"/><text class="field-label" x="60.5" y="86" text-anchor="middle">Hopwright</text><path d="M60.5 90v7m-2-2 2 2 2-2" stroke="#111" fill="none"/><line x1="20" y1="114" x2="101" y2="114" stroke="var(--line)" stroke-width=".6"/></svg></div>
</div>

<p class="section-title" style="left:45px;top:643px">One sided:</p>

<!-- Flat labels -->
<div class="sheet gold" style="left:45px">
  <span class="corner-band"></span><div class="seal"><span>Frask</span></div>
  <p class="name gothic">Frask Ale</p>
  <p class="entry beer">Beer<i></i></p><p class="entry maker">Hopwright<i></i></p>
</div>
<div class="sheet sky" style="left:228px">
  <div class="seal"><span>Frask</span></div>
  <p class="name gothic">Frask Ale</p>
  <p class="entry beer">Beer<i></i></p><p class="entry maker">Hopwright<i></i></p>
</div>
<div class="sheet gold" style="left:423px">
  <span class="corner-band"></span><span class="plain-mark"></span>
  <p class="name gothic">Frask Ale</p>
  <p class="entry beer">Beer<i></i></p><p class="entry maker">Hopwright<i></i></p>
</div>
<div class="sheet gold" style="left:610px;top:681px">
  <span class="corner-band"></span><div class="seal"><span>Frask</span></div>
  <p class="name slab">Frask<br>Ale</p>
  <p class="entry beer">Beer<i></i></p><p class="entry maker">Hopwright<i></i></p>
</div>
<div class="sheet sky" style="left:793px;top:681px">
  <div class="seal"><span>Frask</span></div>
  <p class="name slab">Frask<br>Ale</p>
  <p class="entry beer">Beer<i></i></p><p class="entry maker">Hopwright<i></i></p>
</div>
<div class="sheet gold" style="left:988px;top:681px">
  <span class="plain-mark"></span>
  <p class="name slab" style="top:110px">Frask<br>Ale</p>
  <p class="entry beer">Beer<i></i></p><p class="entry maker">Hopwright<i></i></p>
</div>

</body>
</html>
```